Logo improvement + business card design + Thank you card design

I am looking for 3 jobs

1. need logo quality improvement, the Font used in logo is " Sacramento " ( come up with improved version of it)
2. i want business card design with same logo
3. A Thank you card design for buyers.

Logo tag line is : a mama and papa shop
slogan is : eco-friendly, non-toxic, child safe toys.

Thank card content will be provided later.

```html
<!DOCTYPE html>
<html lang="en">
<head>
<meta charset="utf-8">
<title>Juniper Lane – Business Card</title>
<link href="https://fonts.googleapis.com/css2?family=Tinos&display=swap" rel="stylesheet">
<style>
  :root {
    --page-bg: #ececec;
    --card-navy: #1f1a3b;
    --mint: #7fe0c4;
    --ink-light: #dfe9f2;
    --brand-ink: #c9f3e6;
  }
  * { margin: 0; padding: 0; box-sizing: border-box; }
  html, body {
    width: 1200px;
    height: 933px;
    overflow: hidden;
    background: var(--page-bg);
  }
  .sheet {
    width: 1200px;
    height: 933px;
    display: flex;
    flex-direction: column;
    align-items: center;
    justify-content: center;
    gap: 44px;
  }
  .card {
    position: relative;
    width: 700px;
    height: 400px;
    background: var(--card-navy);
    overflow: hidden;
    box-shadow: 0 10px 30px rgba(0,0,0,0.18);
  }
  .card-stripes {
    position: absolute;
    inset: 0;
    width: 100%;
    height: 100%;
  }
  .brand {
    position: absolute;
    display: flex;
    align-items: center;
    gap: 14px;
  }
  .brand-name {
    font-family: "Tinos", serif;
    font-weight: 400;
    color: var(--brand-ink);
    line-height: 1;
    white-space: nowrap;
    letter-spacing: 1px;
  }
  .brand-dot {
    border-radius: 50%;
    background: var(--mint);
    flex: none;
  }
  /* front */
  .card-front .brand { left: 40px; top: 210px; }
  .card-front .brand-name { font-size: 60px; }
  .card-front .brand-dot { width: 26px; height: 26px; }

  /* back */
  .card-back .brand { right: 30px; bottom: 44px; }
  .card-back .brand-name { font-size: 40px; }
  .card-back .brand-dot { width: 18px; height: 18px; }

  .contact-list {
    position: absolute;
    left: 268px;
    top: 32px;
    list-style: none;
    font-family: "Tinos", serif;
    color: var(--ink-light);
    font-size: 22px;
    line-height: 1.05;
    letter-spacing: 1px;
  }
  .contact-item {
    display: flex;
    align-items: flex-start;
    gap: 14px;
    margin-bottom: 12px;
  }
  .contact-icon {
    width: 26px;
    height: 26px;
    flex: none;
    margin-top: 2px;
  }
</style>
</head>
<body>
<main class="sheet">

  <section class="card card-front" aria-label="Business card front">
    <svg class="card-stripes" viewBox="0 0 700 400" aria-hidden="true">
      <defs>
        <linearGradient id="bandFront" x1="0" y1="0" x2="1" y2="1">
          <stop offset="0" stop-color="#7fe0c4"/>
          <stop offset="0.55" stop-color="#a9eadb"/>
          <stop offset="1" stop-color="#ecebf8"/>
        </linearGradient>
      </defs>
      <polygon points="292,42 318,42 448,138 422,138" fill="#7fe0c4"/>
      <polygon points="326,26 352,26 488,126 462,126" fill="#7fe0c4"/>
      <polygon points="392,0 520,0 700,140 700,200 640,200" fill="url(#bandFront)"/>
      <polygon points="560,0 700,0 700,100" fill="#7fe0c4" opacity="0.9"/>
    </svg>
    <div class="brand">
      <span class="brand-name">Juniper Lane</span>
      <span class="brand-dot"></span>
    </div>
  </section>

  <section class="card card-back" aria-label="Business card back">
    <svg class="card-stripes" viewBox="0 0 700 400" aria-hidden="true">
      <defs>
        <linearGradient id="bandBack" x1="0" y1="0" x2="1" y2="1">
          <stop offset="0" stop-color="#7fe0c4"/>
          <stop offset="0.6" stop-color="#b5ecdf"/>
          <stop offset="1" stop-color="#e8e7f8"/>
        </linearGradient>
      </defs>
      <polygon points="0,262 0,284 208,214 198,196" fill="#7fe0c4"/>
      <polygon points="0,306 0,328 236,244 226,226" fill="#7fe0c4"/>
      <polygon points="40,190 190,122 320,232 320,400 270,400 270,258 200,190 70,238" fill="url(#bandBack)"/>
    </svg>

    <ul class="contact-list">
      <li class="contact-item">
        <svg class="contact-icon" viewBox="0 0 24 24" aria-hidden="true">
          <path d="M6.6 10.8a15 15 0 0 0 6.6 6.6l2.2-2.2a1 1 0 0 1 1-.25 11.4 11.4 0 0 0 3.6.57 1 1 0 0 1 1 1V20a1 1 0 0 1-1 1A17 17 0 0 1 3 4a1 1 0 0 1 1-1h3.5a1 1 0 0 1 1 1c0 1.25.2 2.45.57 3.57a1 1 0 0 1-.25 1z" fill="#dfe9f2"/>
        </svg>
        <span>01710000000<br>01820000000</span>
      </li>
      <li class="contact-item">
        <svg class="contact-icon" viewBox="0 0 24 24" aria-hidden="true" fill="none" stroke="#dfe9f2" stroke-width="1.6">
          <circle cx="12" cy="12" r="9.5"/>
          <ellipse cx="12" cy="12" rx="4.2" ry="9.5"/>
          <line x1="2.5" y1="12" x2="21.5" y2="12"/>
          <line x1="4" y1="7" x2="20" y2="7"/>
          <line x1="4" y1="17" x2="20" y2="17"/>
        </svg>
        <span>www.juniperlane.com</span>
      </li>
      <li class="contact-item">
        <svg class="contact-icon" viewBox="0 0 24 24" aria-hidden="true" fill="none" stroke="#7fe0c4" stroke-width="1.8">
          <path d="M12 22s-7-7.2-7-12a7 7 0 0 1 14 0c0 4.8-7 12-7 12z"/>
          <circle cx="12" cy="10" r="2.6"/>
        </svg>
        <span>45 Garden Road<br>Dhaka-1205</span>
      </li>
    </ul>

    <div class="brand">
      <span class="brand-name">Juniper Lane</span>
      <span class="brand-dot"></span>
    </div>
  </section>

</main>
</body>
</html>
```